To design a illustration tattoo expo poster, Please think about Shanghai is a fashion & modern city, A1 size, poster text below:

2016上海国际墨影狂潮艺术展
Shanghai Inkwave Frenzy & Skin Craft Expo

日期 Date: 9/2-9/4

地点:上海国际锦澜会馆
Venue: Shanghai International Brocade Hall

http://www.inkwavefrenzyfair.example
Email: expo@inkwave-frenzy.example

Target Market(s)

Shanghai, China

Industry/Entity Type

Fashion

Requirements
Must have
• My Project have to design by illustration, and need ai file and font, the text have to provide non-create outline & create outline both file.

```html
<!DOCTYPE html>
<html lang="zh">
<head>
<meta charset="utf-8">
<title>Shanghai Inkwave Frenzy &amp; Skin Craft Expo 2016</title>
<link rel="stylesheet" href="https://fonts.googleapis.com/css2?family=Antonio:wght@300;400&family=Noto+Serif+SC:wght@400&display=swap">
<style>
  :root {
    --backdrop: #e4e1dc;
    --paper: #f4f3f1;
    --ink: #111111;
    --gold: #9c7f55;
    --band: #0d0d0d;
    --band-text: #ffffff;
    --photo-light: #f3f2ef;
    --photo-warm: #d9d1bc;
    --photo-cool: #cdced2;
  }
  * { margin: 0; padding: 0; box-sizing: border-box; }
  html, body {
    width: 1200px; height: 800px; overflow: hidden;
    background: var(--backdrop);
  }
  .poster {
    position: absolute;
    left: 331px; top: 21px;
    width: 537px; height: 758px;
    background: var(--paper);
    overflow: hidden;
    font-family: "Antonio", "Oswald", sans-serif;
    color: var(--ink);
  }
  .photo-area {
    position: absolute;
    left: 0; top: 367px; width: 100%; height: 391px;
    background:
      linear-gradient(180deg, rgba(244,243,241,0.9) 0%, rgba(244,243,241,0) 30%),
      linear-gradient(100deg, var(--photo-warm) 0%, var(--photo-cool) 30%, var(--photo-light) 47%, var(--photo-light) 56%, var(--photo-cool) 72%, var(--photo-warm) 100%);
  }
  .ink-loop {
    position: absolute;
    left: 70px; top: 108px; width: 450px; height: 470px;
    border-radius: 50%;
    background: radial-gradient(ellipse at center, rgba(17,17,17,0) 62%, rgba(17,17,17,0.06) 70%, rgba(17,17,17,0) 78%);
  }
  .year {
    position: absolute; left: 24px; top: 22px;
    font-size: 44px; font-weight: 300; letter-spacing: 12px;
    color: var(--gold); line-height: 1;
  }
  .title-cn {
    position: absolute; left: 24px; top: 76px;
    font-family: "Noto Serif SC", serif; font-size: 15px; letter-spacing: 1px;
    color: var(--ink);
  }
  .title-band {
    position: absolute; left: 0; top: 183px; width: 100%; height: 91px;
    background: var(--band); color: var(--band-text);
    padding: 8px 0 0 22px;
    font-size: 31px; font-weight: 400; letter-spacing: 8px; line-height: 42px;
    white-space: nowrap;
  }
  .date {
    position: absolute; left: 118px; top: 308px;
    font-size: 24px; letter-spacing: 7px; font-weight: 300;
  }
  .date .cn { font-family: "Noto Serif SC", serif; font-size: 27px; letter-spacing: 2px; margin-right: 16px; }
  .venue {
    position: absolute; left: 0; width: 100%; top: 662px;
    text-align: center; line-height: 1;
  }
  .venue .en { font-size: 15px; letter-spacing: 5px; white-space: nowrap; }
  .venue .cn { font-family: "Noto Serif SC", serif; font-size: 17px; margin-top: 7px; letter-spacing: 1px; }
  .contact {
    position: absolute; left: 0; width: 100%; top: 718px;
    text-align: center; font-size: 10px; letter-spacing: 1.5px; line-height: 14px;
  }
</style>
</head>
<body>
<main class="poster">
  <div class="photo-area" role="img" aria-label="Photograph of two modern glass skyscrapers seen from below, converging toward a bright sky"></div>
  <div class="ink-loop" role="img" aria-label="Hand-drawn loose circular ink loop in black lines"></div>

  <div class="year">2016</div>
  <div class="title-cn">上海国际墨影狂潮艺术展</div>

  <h1 class="title-band">SHANGHAI INKWAVE FRENZY<br>&amp; SKIN CRAFT EXPO</h1>

  <div class="date"><span class="cn">日期</span>DATE: 9/2-9/4</div>

  <div class="venue">
    <div class="en">VENUE: SHANGHAI INTERNATIONAL BROCADE HALL</div>
    <div class="cn">地点：上海国际锦澜会馆</div>
  </div>

  <div class="contact">
    HTTP://WWW.INKWAVEFRENZYFAIR.EXAMPLE<br>
    EMAIL: EXPO@INKWAVE-FRENZY.EXAMPLE
  </div>
</main>
</body>
</html>
```